Juniper Estates - wanted BRILLIANT website design for our new property investing company

We need a website design for our new company based in Bristol, England, UK called "Juniper Estates". We help buy people property who are in financial difficulty or who are needing to sell their property quickly for reasons such as death, divorce/separation, relocation, emigration.

We have a logo being designed incorporating strawberry and property (so red and green). We would like designs to communicate an elegant ,professional, approachable, friendly
fresh clean but also warm appealing appearance
Not too busy
Website consistent with logo and company name i.e. colour scheme

Please use our word document for content as a guide but use professional judgement for minor alterations if you feel they would benefit the site/structure etc

Please ask at any time if not sure

Target Market(s)

Adult british population, those that have a mortgage / loan / own property

Industry/Entity Type

Financial

Font styles to use
Serif
Sans Serif
Decorative

Colors
0692cd
33b7a4
acd036
fbee3e
3176b5
886aae
a6479a
e567a6
eb1f27

Requirements
Must have
• This must not look like a template website we are looking for UNIQUE please!
Nice to have
• Bristol pictures instead of generic, or colourful line drawings/comic drawings of houses/property/keys/happy people.....
Should not have
• An obvious off the shelf template design

```html
<!DOCTYPE html>
<html lang="en">
<head>
<meta charset="utf-8">
<title>Juniper Estates</title>
<link rel="stylesheet" href="https://fonts.googleapis.com/css2?family=Marcellus&family=Didact+Gothic&family=Arimo:wght@400;700&family=Open+Sans:wght@700&display=swap">
<style>
:root{
  --red:#d7262b;
  --red-dark:#b81d22;
  --green:#47ad1d;
  --green-bright:#5cc42a;
  --slate:#3a4449;
  --slate-dark:#2c3438;
  --bar:#22292c;
  --black:#151819;
  --ink:#111;
  --white:#fff;
  --field-border:#dcdcdc;
}
*{box-sizing:border-box;margin:0;padding:0}
html,body{width:804px;height:1200px;overflow:hidden;background:var(--white)}
body{position:relative;font-family:Arimo,Arial,sans-serif;color:var(--ink)}
.abs{position:absolute}

/* top strip */
.top-strip{left:0;top:0;width:804px;height:23px;background:var(--bar);border-top:3px solid var(--red)}
.top-contact{right:64px;top:5px;display:flex;gap:14px;font-size:8.5px;color:var(--white);align-items:center}
.top-contact span{display:flex;align-items:center;gap:6px}
.top-contact .phone{font-size:10px}

/* header */
.brand-band{left:0;top:23px;width:804px;height:39px;background:var(--slate)}
.brand{left:131px;top:9px;font-family:"Open Sans",Arial,sans-serif;font-weight:700;font-size:18.5px;color:var(--white);letter-spacing:.2px}

/* nav */
.main-nav{left:0;top:62px;width:804px;height:30px;background:var(--slate-dark);border-top:1px solid #1b2124;border-bottom:1px solid #1b2124}
.nav-list{position:absolute;left:121px;top:0;display:flex;list-style:none;height:28px}
.nav-list li{font-size:8px;color:var(--white);padding:0 13px;line-height:28px}
.nav-list li.active{background:var(--green)}

/* hero */
.hero{left:0;top:92px;width:804px;height:285px;background:linear-gradient(180deg,#6e5a82 0%,#8a6b7e 30%,#5a4638 62%,#3a3026 80%,#4f6f8a 100%)}
.hero-caption{left:137px;top:225px;width:343px;height:76px;background:rgba(40,40,40,.72);padding:6px 12px}
.hero-caption .line1{font-family:"Didact Gothic",Arial,sans-serif;font-size:29px;color:var(--white);line-height:32px;letter-spacing:-.5px}
.hero-caption .line2{font-family:"Didact Gothic",Arial,sans-serif;font-size:31px;color:var(--green-bright);line-height:34px;font-weight:700;letter-spacing:-.6px}
.hero-arrow{left:482px;width:32px;height:31px}
.hero-arrow.prev{top:233px;background:var(--red)}
.hero-arrow.next{top:266px;background:var(--green)}

/* welcome band */
.welcome-band{left:0;top:377px;width:804px;height:98px;background:var(--red);border-bottom:1px solid var(--red-dark)}
.welcome-band h2{position:absolute;left:131px;top:4px;font-family:Marcellus,Georgia,serif;font-weight:400;font-size:26px;color:var(--white)}
.welcome-band p{position:absolute;left:131px;top:37px;width:550px;font-size:9.6px;line-height:16.5px;color:var(--white)}

/* intro */
.intro{left:133px;top:494px;width:340px}
.intro h3{font-family:Marcellus,Georgia,serif;font-size:15px;line-height:18px;font-weight:700;width:260px}
.intro .lead{font-family:Marcellus,Georgia,serif;font-size:12.5px;margin-top:2px}
.services{list-style:none;margin-top:11px}
.services li{font-family:Marcellus,Georgia,serif;font-size:9px;line-height:15.8px}
.services li::before{content:"• "}

/* contact form */
.contact-form{left:121px;top:733px;width:300px}
.contact-form h4{position:absolute;left:31px;top:0;font-family:Marcellus,Georgia,serif;font-weight:400;font-size:13px}
.field-label{position:absolute;width:77px;text-align:right;font-family:Marcellus,Georgia,serif;font-size:8.5px}
.field{position:absolute;left:88px;width:204px;height:20px;border:1px solid var(--field-border);background:var(--white)}
.field.message{height:71px}
.btn-dark{position:absolute;left:88px;top:229px;width:45px;height:17px;border-radius:3px;background:linear-gradient(#444,#111);color:var(--white);font-size:9px;text-align:center;line-height:17px}

/* sidebar */
.help-panel{left:494px;top:496px;width:177px;height:493px;background:var(--slate);border:1px solid #2a3235}
.help-panel h3{position:absolute;left:9px;top:8px;font-family:Marcellus,Georgia,serif;font-weight:700;font-size:17px;color:var(--white)}
.help-list{position:absolute;left:7px;top:36px;list-style:none}
.help-list li{width:164px;height:22px;background:var(--white);margin-bottom:7.9px;font-family:Marcellus,Georgia,serif;font-size:8px;line-height:22px;padding-left:7px;letter-spacing:.2px}
.btn-red{position:absolute;left:8px;top:461px;width:45px;height:19px;border-radius:4px;background:linear-gradient(#e8403f,#c41e21);color:var(--white);font-family:"Open Sans",Arial,sans-serif;font-weight:700;font-size:9.5px;text-align:center;line-height:19px}

/* footer */
.footer{left:0;top:1030px;width:804px;height:140px;background:var(--slate-dark);border-top:4px solid var(--green)}
.footer-nav{position:absolute;left:198px;top:2px;display:flex;list-style:none;height:28px}
.footer-nav li{font-size:7.8px;color:var(--white);padding:0 11px;line-height:28px}
.footer-nav li.active{background:var(--green)}
.footer-brand{position:absolute;left:121px;top:48px;font-family:"Open Sans",Arial,sans-serif;font-weight:700;font-size:13.5px;color:var(--white)}
.footer-bodies{position:absolute;left:124px;top:70px;font-size:7.6px;line-height:12px;color:var(--white)}
.footer-contact{position:absolute;left:318px;top:45px;width:200px;text-align:center;color:var(--white);font-size:9.5px;line-height:13px}
.footer-contact h5{font-family:Arimo,Arial,sans-serif;font-size:12.5px;color:var(--green-bright);margin-bottom:5px;letter-spacing:.3px}
.map{position:absolute;left:522px;top:37px;width:152px;height:94px;background:linear-gradient(135deg,#dfe3d6,#efe9cf 55%,#d8dccb);border:1px solid #fff}
.base-bar{left:0;top:1170px;width:804px;height:30px;background:var(--black);display:flex;justify-content:center;align-items:center;gap:5px;color:var(--white);font-size:8px}
.social{width:19px;height:19px;border-radius:2px}
.social.one{background:#3b5a98;margin-left:3px}
.social.two{background:#4fb6e6}
</style>
</head>
<body>

<header>
  <div class="abs top-strip">
    <div class="abs top-contact">
      <span>
        <svg width="10" height="7" viewBox="0 0 10 7"><rect x=".5" y=".5" width="9" height="6" fill="none" stroke="#8cc63f"/><path d="M.5 .5 5 4 9.5 .5" fill="none" stroke="#8cc63f"/></svg>
        hello@juniper-estates.co.uk
      </span>
      <span class="phone">
        <svg width="8" height="9" viewBox="0 0 8 9"><path d="M1.5 0 3 2 2 3.2c.6 1.4 1.6 2.6 3 3.3L6 5.4 8 7 7 8.8C3.5 8.4.2 5 0 1.5Z" fill="#8cc63f"/></svg>
        07700 900318
      </span>
    </div>
  </div>
  <div class="abs brand-band"><div class="abs brand">JUNIPER ESTATES</div></div>
  <nav class="abs main-nav">
    <ul class="nav-list">
      <li class="active">Home</li><li>Sell Your Property Fast</li><li>Rent Your Property Fast</li><li>Common Questions</li><li>About Us</li><li>Contact Us</li>
    </ul>
  </nav>
</header>

<section class="abs hero" role="img" aria-label="Photograph of a large lit family home at dusk with a swimming pool and terrace"></section>
<div class="abs hero-caption">
  <div class="line1">WELCOME TO</div>
  <div class="line2">JUNIPER ESTATES</div>
</div>
<svg class="abs hero-arrow prev" viewBox="0 0 32 31"><path d="M22 7 10 15.5 22 24" fill="none" stroke="#fff" stroke-width="1.3"/></svg>
<svg class="abs hero-arrow next" viewBox="0 0 32 31"><path d="M10 7 22 15.5 10 24" fill="none" stroke="#fff" stroke-width="1.3"/></svg>

<section class="abs welcome-band">
  <h2>WELCOME</h2>
  <p>Lorem ipsum dolor sit amet, consectetur adipisicing elit, sed do eiusmod tempor incididunt ut labore et dolore magna aliqua. Ut enim ad minim veniam, quis nostrud exercitation ullamco laboris nisi ut aliquip ex ea commodo consequat. Duis aute irure dolor in reprehenderit in voluptate velit esse cillum dolore eu fugiat nulla pariatur.</p>
</section>

<section class="abs intro">
  <h3>Do you want to sell or rent out your house quickly?</h3>
  <p class="lead">We are a local family run property business who specialize in</p>
  <ul class="services">
    <li>Buying properties quickly</li>
    <li>Finding creative solutions to your property problems</li>
    <li>Property rental management</li>
    <li>Lettings to professional and student tenants</li>
    <li>Guaranteed rent and management schemes for landlords</li>
    <li>STOPPING repossessions</li>
    <li>Motivated sellers</li>
    <li>Chain fixing</li>
    <li>Negative equity problems</li>
  </ul>
</section>

<section class="abs contact-form">
  <h4>Contact form</h4>
  <span class="field-label" style="top:38px">Your Name:</span><span class="field" style="top:32px"></span>
  <span class="field-label" style="top:67px">Email Address:</span><span class="field" style="top:61px"></span>
  <span class="field-label" style="top:96px">Phone number:</span><span class="field" style="top:90px"></span>
  <span class="field-label" style="top:125px">Property address:</span><span class="field" style="top:119px"></span>
  <span class="field-label" style="top:145px">Message:</span><span class="field message" style="top:148px"></span>
  <span class="btn-dark">SUBMIT</span>
</section>

<aside class="abs help-panel">
  <h3>Who can we help?</h3>
  <ul class="help-list">
    <li>HOW TO STOP REPOSSESSION</li>
    <li>DIVORCE OR SEPARATION</li>
    <li>FINANCIAL PROBLEMS</li>
    <li>DON'T LIKE ESTATE AGENTS?</li>
    <li>PROPERTY NEEDING WORK</li>
    <li>RETIRING LANDLORDS</li>
    <li>NEGATIVE EQUITY</li>
    <li>OPPORTUNITY NOT TO BE MISSED!!</li>
    <li>GUARANTEED RENT SCHEME</li>
    <li>ILL HEALTH</li>
    <li>RELOCATING</li>
    <li>INHERITED PROPERTY</li>
    <li>CHAIN COLLAPSE</li>
    <li>TENANTED PROPERTY</li>
  </ul>
  <span class="btn-red">SUBMIT</span>
</aside>

<footer class="abs footer">
  <ul class="footer-nav">
    <li class="active">Home</li><li>Sell Your Property Fast</li><li>Rent Your Property Fast</li><li>Common Questions</li><li>About Us</li><li>Contact Us</li>
  </ul>
  <div class="footer-brand">JUNIPER ESTATES</div>
  <div class="footer-bodies">RCSA (Register of Certified Surveying Advisers),<br>LLF (Landlords' Lettings Forum),<br>The Housing Redress Panel</div>
  <div class="footer-contact">
    <h5>CONTACT US</h5>
    2014 Juniper Estates Limited.<br>Reg No 4471203<br>07700 900318<br>hello@juniper-estates.co.uk
  </div>
  <div class="map" role="img" aria-label="Street map showing the office location"></div>
</footer>

<div class="abs base-bar">
  FOLLOW US:
  <span class="social one" aria-label="Social profile"></span>
  <span class="social two" aria-label="Social profile"></span>
</div>

</body>
</html>
```